Modern Business Card for Lanternfield 2018

Our company assumes the best about people. We are creating an online community of entrepreneurs and business leaders who struggle with marketing their business online.

This business card should POP! We recently got a new logo and are launching a new website next month, so our business cards should make a statement that feels:
-Fresh
-Smart
-Trustworthy
-Fun

Target Market(s)

small business owners, entrepreneurs

Industry/Entity Type

Digital Marketing

Contact Information for Business Card

Dimensions: 3.5" x 2"

Font styles to use
Sans Serif

Colors
f37122
ffffff

Requirements
Must have
• We need a business card with a modern, bold design. We will use one side of the card as a lead-generation offer, so text on one side will need to fit up to 140 characters. The business card should stick to our core colors (orange, black, and white).
Nice to have
• We think a vertical "portrait" design could be interesting.
Should not have
• Should not look like a traditional business card. The round icon should stand out from a distance.

```html
<!DOCTYPE html>
<html lang="en">
<head>
<meta charset="utf-8">
<title>Lanternfield Business Card</title>
<link rel="stylesheet" href="https://fonts.googleapis.com/css2?family=Montserrat:wght@800&family=Lato:wght@400&family=Open+Sans:wght@400;700&family=Kalam:wght@400&display=swap">
<style>
  :root {
    --orange: #f37122;
    --white: #ffffff;
    --ink: #555555;
    --rule: #d9d9d9;
    --backdrop: #2b2b2b;
  }
  * { margin: 0; padding: 0; box-sizing: border-box; }
  html, body { width: 1200px; height: 1200px; overflow: hidden; }
  body { background: var(--backdrop); position: relative; }

  .card {
    position: absolute;
    top: 310px;
    height: 594px;
    background: var(--white);
    text-align: center;
    overflow: hidden;
  }
  .card--front { left: 234px; width: 364px; }
  .card--back { left: 627px; width: 369px; }

  .brand-dot {
    width: 50px; height: 50px; border-radius: 50%;
    background: var(--orange);
    margin: 93px auto 0;
  }
  .brand-name {
    margin-top: 20px;
    font-family: "Montserrat", sans-serif;
    font-weight: 800;
    font-size: 35px;
    letter-spacing: 0.5px;
    color: var(--orange);
    line-height: 1;
  }
  .tagline {
    margin-top: 8px;
    font-family: "Kalam", cursive;
    font-size: 15px;
    letter-spacing: 1.5px;
    text-transform: uppercase;
    color: var(--orange);
  }
  .person-name {
    margin-top: 68px;
    font-family: "Kalam", cursive;
    font-size: 24px;
    letter-spacing: 1.5px;
    text-transform: uppercase;
    color: var(--orange);
    line-height: 1.1;
  }
  .person-title, .contact {
    font-family: "Lato", sans-serif;
    text-transform: uppercase;
    color: var(--ink);
  }
  .person-title { font-size: 17px; letter-spacing: 0.5px; margin-top: 2px; }
  .divider {
    width: 264px; height: 1px; background: var(--rule);
    margin: 19px auto;
  }
  .contact { font-size: 17px; line-height: 27px; }
  .benefits {
    font-family: "Lato", sans-serif;
    font-size: 17px;
    line-height: 25px;
    text-transform: uppercase;
    color: var(--orange);
    margin-top: 20px;
  }

  .back-name {
    position: absolute; left: 0; right: 0; top: 255px;
    font-family: "Montserrat", sans-serif;
    font-weight: 800;
    font-size: 26px;
    color: var(--orange);
  }
  .back-dot {
    position: absolute; left: 136px; top: 303px;
    width: 96px; height: 96px; border-radius: 50%;
    background: var(--orange);
  }
  .offer-band {
    position: absolute; left: 0; right: 0; bottom: 0; height: 199px;
    background: var(--orange);
    color: var(--white);
    font-family: "Open Sans", sans-serif;
    padding-top: 40px;
  }
  .offer-text { font-size: 20px; line-height: 27px; }
  .offer-link { font-weight: 700; font-size: 21px; margin-top: 18px; }
</style>
</head>
<body>
  <section class="card card--front">
    <div class="brand-dot"></div>
    <h1 class="brand-name">LANTERNFIELD</h1>
    <p class="tagline">Share ideas that spark growth</p>
    <p class="person-name">Dana Whitlock</p>
    <p class="person-title">Story Marketing Coach</p>
    <div class="divider"></div>
    <p class="contact">dana@lanternfieldhq.com<br>www.lanternfieldhq.com</p>
    <div class="divider"></div>
    <p class="benefits">Find more clients<br>Grow your revenue<br>Build lasting trust.</p>
  </section>

  <section class="card card--back">
    <p class="back-name">LANTERNFIELD</p>
    <div class="back-dot"></div>
    <div class="offer-band">
      <p class="offer-text">Get your free Lanternfield<br>Starter Package and our<br>marketing guide today at</p>
      <p class="offer-link">lanternfieldhq.com/start</p>
    </div>
  </section>
</body>
</html>
```